Bref créative
bluetidal business card
business card for bluetidal.example
Professional
Margaret Pellowin
General Manager
p.o.box 4872 - 519 Maplecrest Ct Nw
garnok77@mailzone.example
http://www.bluetidal.example/
bluetidal logo

```html
<!DOCTYPE html>
<html lang="en">
<head>
<meta charset="utf-8">
<title>bluetidal business card</title>
<link href="https://fonts.googleapis.com/css2?family=Arimo:wght@400;700&display=swap" rel="stylesheet">
<style>
  :root {
    --backdrop: #4a2a1c;
    --card: #ffffff;
    --ink: #1c1c1c;
    --yellow: #f6c400;
    --red: #e2392d;
    --blue: #27a3dc;
    --orange: #f39221;
  }
  * { margin: 0; padding: 0; box-sizing: border-box; }
  html, body { width: 1200px; height: 749px; overflow: hidden; }
  body {
    background: var(--backdrop);
    font-family: "Arimo", Arial, sans-serif;
    color: var(--ink);
    position: relative;
  }
  .card {
    position: absolute;
    top: 240px;
    width: 480px;
    height: 302px;
    background: var(--card);
    box-shadow: 0 4px 14px rgba(0,0,0,0.45);
    overflow: hidden;
  }
  .card--vertical { left: 101px; }
  .card--horizontal { left: 612px; }

  .brand {
    position: absolute;
    left: 16px;
    top: 30px;
    font-weight: 700;
    font-size: 22px;
    color: var(--ink);
  }

  .holder { position: absolute; }
  .holder__name { font-weight: 700; font-size: 19px; line-height: 1.1; white-space: nowrap; }
  .holder__title { font-size: 10px; margin-top: 3px; }

  .contact {
    position: absolute;
    font-size: 10px;
    line-height: 1.35;
    white-space: nowrap;
  }
  .contact__row span { display: inline-block; width: 38px; }

  .card--vertical .holder { left: 294px; top: 38px; }
  .card--vertical .contact { left: 294px; top: 173px; }
  .card--horizontal .holder { left: 204px; top: 114px; }
  .card--horizontal .contact { left: 204px; top: 164px; }

  .stripes { position: absolute; }
  .stripes--vertical { left: 236px; top: 0; height: 100%; display: flex; gap: 5px; }
  .stripes--vertical i { width: 6px; height: 100%; display: block; }
  .stripes--horizontal { left: 0; right: 0; top: 240px; display: flex; flex-direction: column; gap: 4px; }
  .stripes--horizontal i { height: 5px; display: block; }
  .c-yellow { background: var(--yellow); }
  .c-red { background: var(--red); }
  .c-blue { background: var(--blue); }
  .c-orange { background: var(--orange); }
</style>
</head>
<body>
  <section class="card card--vertical">
    <div class="brand">bluetidal</div>
    <div class="stripes stripes--vertical"><i class="c-yellow"></i><i class="c-red"></i><i class="c-orange"></i><i class="c-blue"></i></div>
    <div class="holder">
      <div class="holder__name">Margaret Pellowin</div>
      <div class="holder__title">General Manager</div>
    </div>
    <div class="contact">
      <div>P.O.Box 4872 - 519 Maplecrest Ct Nw</div>
      <div class="contact__row"><span>Pone:</span>555-014-0001</div>
      <div class="contact__row"><span>Fax:</span>555-014-06221</div>
      <div>Email: garnok77@mailzone.example</div>
      <div>http://www.bluetidal.example/</div>
    </div>
  </section>

  <section class="card card--horizontal">
    <div class="brand">bluetidal</div>
    <div class="holder">
      <div class="holder__name">Margaret Pellowin</div>
      <div class="holder__title">General Manager</div>
    </div>
    <div class="contact">
      <div>P.O.Box 4872 - 519 Maplecrest Ct Nw</div>
      <div class="contact__row"><span>Pone:</span>555-014-0001</div>
      <div class="contact__row"><span>Fax:</span>555-014-06221</div>
      <div>Email: garnok77@mailzone.example</div>
      <div>http://www.bluetidal.example/</div>
    </div>
    <div class="stripes stripes--horizontal"><i class="c-red"></i><i class="c-yellow"></i><i class="c-blue"></i><i class="c-orange"></i></div>
  </section>
</body>
</html>
```